Quorvex - Automated robotic Inspection with AI need new business cards

We need a new design of our business cards. The company is focused on automated quality control at high speed with unmatched results. We have a logo but need a more forward leaning business card that shows that we are delivering cutting edge technology.

Contact Information for Business Card

Name
Position
Adress
Phone
Email
e.g.
Lena Holmqvist
Chief Financial Officer (CFO)

Quorvex Sweden AB
Bruksvägen 14, SE-175 43 JÄRFÄLLA, Sweden
Mobile: +46735 21 47 83 | Office: +46 8 61 94 27
www.quorvex-example.com

Font styles to use
Sans Serif

```html
<!DOCTYPE html>
<html lang="en">
<head>
<meta charset="utf-8">
<title>Quorvex Business Card</title>
<link href="https://fonts.googleapis.com/css2?family=Roboto:ital,wght@0,400;0,500;0,700;1,400;1,500&display=swap" rel="stylesheet">
<style>
  :root {
    --brand-blue: #29628b;
    --card-white: #ffffff;
    --backdrop: #e6e8eb;
    --text-light: #ffffff;
  }
  * { margin: 0; padding: 0; box-sizing: border-box; }
  html, body { width: 1200px; height: 900px; overflow: hidden; }
  body {
    background: var(--backdrop);
    font-family: "Roboto", sans-serif;
    position: relative;
  }
  .card {
    position: absolute;
    left: 250px;
    width: 700px;
    height: 400px;
    overflow: hidden;
    box-shadow: 0 6px 18px rgba(0,0,0,0.18);
  }
  .card-front { top: 35px; background: var(--card-white); }
  .card-back { top: 465px; background: var(--brand-blue); }

  .front-waves { position: absolute; inset: 0; }

  .front-brand {
    position: absolute;
    left: 48px;
    top: 42px;
    display: flex;
    align-items: center;
    gap: 14px;
    color: var(--brand-blue);
  }
  .brand-dot {
    width: 34px; height: 34px;
    border-radius: 50%;
    background: var(--brand-blue);
  }
  .brand-name {
    font-weight: 500;
    font-size: 46px;
    letter-spacing: 1px;
    line-height: 1;
  }

  .holder {
    position: absolute;
    left: 34px;
    top: 262px;
    color: var(--text-light);
  }
  .holder-name { font-weight: 700; font-size: 27px; line-height: 1.1; }
  .holder-title { font-style: italic; font-size: 15px; margin-top: 4px; }

  .contact {
    position: absolute;
    left: 320px;
    top: 250px;
    color: var(--text-light);
    font-size: 12.5px;
    line-height: 17px;
    list-style: none;
  }
  .contact li { display: flex; align-items: center; gap: 7px; white-space: nowrap; }
  .contact .icon { width: 12px; height: 12px; flex: none; }
  .contact .no-icon { padding-left: 19px; }

  .back-brand {
    position: absolute;
    left: 0; right: 0;
    top: 130px;
    display: flex;
    justify-content: center;
    align-items: center;
    gap: 20px;
    color: var(--text-light);
  }
  .back-brand .brand-dot { width: 52px; height: 52px; background: var(--text-light); }
  .back-brand .brand-name { font-size: 84px; }
  .back-web {
    position: absolute;
    left: 0; right: 0;
    top: 272px;
    text-align: center;
    color: var(--text-light);
    font-size: 16px;
    letter-spacing: 1px;
  }
  .back-rule {
    width: 70px;
    height: 2px;
    background: var(--text-light);
    margin: 10px auto 0;
  }
</style>
</head>
<body>

<section class="card card-front">
  <svg class="front-waves" width="700" height="400" viewBox="0 0 700 400" aria-hidden="true">
    <path d="M0,110 C120,230 330,225 470,225 C580,225 640,300 660,400 L0,400 Z" fill="var(--brand-blue)"/>
    <path d="M0,118 C120,234 330,230 470,230 C572,230 628,300 645,400" fill="none" stroke="var(--card-white)" stroke-width="3"/>
    <path d="M0,92 C125,214 335,210 475,211 C590,212 655,290 680,400" fill="none" stroke="var(--brand-blue)" stroke-width="5"/>
  </svg>

  <div class="front-brand">
    <span class="brand-dot"></span>
    <span class="brand-name">Quorvex</span>
  </div>

  <div class="holder">
    <p class="holder-name">Lena Holmqvist</p>
    <p class="holder-title">Chief Financial Officer (CFO)</p>
  </div>

  <ul class="contact">
    <li class="no-icon">Quorvex Sweden AB</li>
    <li class="no-icon">Bruksvägen 14, SE-175 43 JÄRFÄLLA</li>
    <li class="no-icon">Sweden</li>
    <li>
      <svg class="icon" viewBox="0 0 12 12"><path d="M2.5,1 L4.5,1 L5.2,3.6 L4,4.6 C4.6,6 6,7.4 7.4,8 L8.4,6.8 L11,7.5 L11,9.5 C11,10.3 10.3,11 9.5,11 C5,11 1,7 1,2.5 C1,1.7 1.7,1 2.5,1 Z" fill="var(--text-light)"/></svg>
      +46 8 61 94 27
    </li>
    <li>
      <svg class="icon" viewBox="0 0 12 12"><rect x="3" y="0.5" width="6" height="11" rx="1" fill="none" stroke="var(--text-light)" stroke-width="1.2"/><circle cx="6" cy="9.5" r="0.7" fill="var(--text-light)"/></svg>
      +46735 21 47 83
    </li>
    <li>
      <svg class="icon" viewBox="0 0 12 12"><rect x="0.5" y="2" width="11" height="8" fill="var(--text-light)"/><path d="M0.5,2 L6,6.5 L11.5,2" fill="none" stroke="var(--brand-blue)" stroke-width="1"/></svg>
      l_holmqvist@quorvex-example.com
    </li>
    <li>
      <svg class="icon" viewBox="0 0 12 12"><circle cx="6" cy="6" r="5.2" fill="none" stroke="var(--text-light)" stroke-width="1"/><ellipse cx="6" cy="6" rx="2.3" ry="5.2" fill="none" stroke="var(--text-light)" stroke-width="0.9"/><path d="M0.8,6 H11.2 M1.8,3.3 H10.2 M1.8,8.7 H10.2" stroke="var(--text-light)" stroke-width="0.9"/></svg>
      www.quorvex-example.com
    </li>
  </ul>
</section>

<section class="card card-back">
  <div class="back-brand">
    <span class="brand-dot"></span>
    <span class="brand-name">Quorvex</span>
  </div>
  <div class="back-web">
    www.quorvex-example.com
    <div class="back-rule"></div>
  </div>
</section>

</body>
</html>
```